Web site for Copper Lantern Cleaner and Protectant

We need a website for a new company called Copper Lantern, LLC. We make and resell a simple spray and wipe waterless all purpose cleaner a protectant safe on all surfaces for use on RVs, boats, cars and motorcycles. This is an eco-friendly green product.

The website will be our store front with product info, training videos, events, social media feeds, and link to our markets space for purchases. We will be working to establish distributers and resellers and as such will be traveling to RV and car shows heavily the first couple of years.

It cleans and protects in a simple spray and wipe step leaving the surface protected and conditioned to repel dust, dirt, water, smudges, bugs and fingerprints while preventing fogging. Safe on acrylic, clarivex, durimon, plastic, rubber, painted surfaces, chrome, stainless, aluminum, vinyl, leather, glass.... This is an eco-friendly green product.

We want to play off the company name to tell the consumer that the product is easy to use and associate to the nostalgics 1950's in the USA.

Attached is our Logo and draft of the labels we will be using for the products. Please let me know what other information you need to get started.

Thank you

```html
<!DOCTYPE html>
<html lang="en">
<head>
<meta charset="utf-8">
<title>Copper Lantern – Waterless All Purpose Cleaner &amp; Protectant</title>
<link href="https://fonts.googleapis.com/css2?family=Roboto:wght@400;500;700&display=swap" rel="stylesheet">
<style>
:root{
  --blue:#1a7fc8;
  --blue-dark:#0f5f9e;
  --green:#3c9a3f;
  --green-band:#4aa84e;
  --ink:#2a2a2a;
  --muted:#555;
  --hero-dark:#2e2e2e;
  --footer:#2b2b2b;
  --gray-band:#e3e3e3;
}
*{box-sizing:border-box;margin:0;padding:0}
html,body{width:743px;height:1200px;overflow:hidden;background:#fff}
body{font-family:'Roboto',Arial,sans-serif;color:var(--ink);position:relative}
.abs{position:absolute}

/* header */
.top-line{left:0;top:0;width:743px;height:3px;background:var(--blue)}
.account-tab{top:0;height:17px;font-size:9px;font-weight:700;color:#fff;display:flex;align-items:center;justify-content:center;gap:5px;clip-path:polygon(8% 0,92% 0,100% 100%,0 100%)}
.account-tab.login{left:512px;width:80px;background:var(--blue)}
.account-tab.register{left:594px;width:68px;background:#333}
.brand{left:84px;top:16px;width:140px;font-size:23px;line-height:25px;font-weight:700;color:var(--blue)}
.phone{left:574px;top:37px;font-size:12px;font-weight:700;color:#333;display:flex;align-items:center;gap:6px}
.main-nav{left:190px;top:64px;width:553px;height:28px;background:linear-gradient(#2b94d8,#1170b6);display:flex;padding-left:52px}
.main-nav a{color:#fff;text-decoration:none;font-size:10px;font-weight:500;display:flex;align-items:center;justify-content:center;border-right:1px solid rgba(255,255,255,.25)}
.main-nav a.active{background:linear-gradient(#4cae4f,#3a923c)}

/* hero */
.hero{left:0;top:92px;width:743px;height:268px;background:radial-gradient(ellipse at 60% 35%,#5a5a5a,var(--hero-dark) 70%)}
.art-car{left:0;top:40px;width:235px;height:170px;background:linear-gradient(135deg,#d8d8d8,#1b1b1b 55%,#0e0e0e);border-radius:0 60px 30px 0}
.art-bottles{left:148px;top:160px;width:78px;height:92px;background:linear-gradient(#fafafa,#cfd6dc);border-radius:8px}
.art-truck{left:246px;top:10px;width:420px;height:160px;background:linear-gradient(90deg,#4db04f 0 55%,#e9ede9 55%);border-radius:30px 60px 12px 12px;opacity:.9}
.art-photo{left:248px;top:171px;width:128px;height:82px;border:2px solid #ddd;border-radius:6px;background:linear-gradient(120deg,#f3f3f3,#5d5f5a 60%,#2a2d27)}
.shop-btn{left:395px;top:195px;width:212px;height:36px;background:linear-gradient(#3aa0e6,#1169b0);border-radius:4px;color:#fff;font-size:19px;font-weight:700;display:flex;align-items:center;padding-left:12px}
.shop-diamond{left:596px;top:184px;width:56px;height:56px;transform:rotate(45deg);border:3px solid #fff;outline:2px solid var(--blue);background:linear-gradient(#e8eef3,#9fb7c7)}
.caption-bar{left:0;top:360px;width:743px;height:23px;background:#161616}
.caption-bar h2{position:absolute;left:82px;top:3px;font-size:14px;font-weight:700;color:#fff}
.slider-dots{position:absolute;left:598px;top:6px;display:flex;gap:9px}
.slider-dots i{width:9px;height:9px;background:#fff;transform:rotate(45deg)}
.slider-dots i.on{background:var(--blue);outline:1px solid #fff}

/* categories */
.categories{left:0;top:383px;width:743px;height:163px;background:var(--gray-band)}
.category{position:absolute;top:22px;width:120px;text-align:center}
.category .diamond{margin:8px auto 0;width:70px;height:70px;transform:rotate(45deg);border:3px solid var(--blue);background:linear-gradient(#8b8b8b,#c8c8c8)}
.category .photo{position:absolute;left:2px;top:28px;width:100px;height:52px;border-radius:6px}
.category span{display:block;margin-top:36px;font-size:12px;font-weight:700;color:#222}

/* sections */
.section-title{left:0;width:743px;text-align:center;font-size:17px;font-weight:700;color:#222}
.section-title .b{color:var(--blue)}.section-title .g{color:var(--green)}
.divider{left:250px;width:243px;height:14px}
.divider::before{content:"";position:absolute;left:0;right:0;top:6px;height:2px;background:linear-gradient(90deg,transparent,#c9c9c9,transparent)}
.divider::after{content:"";position:absolute;left:116px;top:1px;width:11px;height:11px;transform:rotate(45deg);background:linear-gradient(#9cc4de,#6e9fbe);border:1px solid #fff}
.lead{left:92px;width:560px;text-align:center;font-size:9px;line-height:12.5px;color:#333}
.video-section{left:0;top:655px;width:743px;height:360px;background:linear-gradient(#fafafa,#e8e8e8);border-top:1px solid #ddd}
.monitor{left:180px;top:743px;width:383px;height:248px;border-radius:8px;background:#1c1c1c}
.monitor-chin{left:180px;top:955px;width:383px;height:36px;border-radius:0 0 8px 8px;background:linear-gradient(#e4e4e4,#bdbdbd)}
.monitor-stand{left:330px;top:991px;width:85px;height:22px;background:linear-gradient(#d8d8d8,#a9a9a9);clip-path:polygon(10% 0,90% 0,100% 100%,0 100%)}
.video-screen{left:194px;top:757px;width:356px;height:183px;background:radial-gradient(circle at 40% 60%,#e8ecef,#59604f 45%,#1d231a)}
.play-btn{left:340px;top:827px;width:44px;height:44px;transform:rotate(45deg);background:rgba(120,120,120,.6)}

/* news band */
.news-band{left:0;top:1015px;width:743px;height:127px;background:linear-gradient(#58b45b,#43a046)}
.band-title{font-size:14px;font-weight:700;color:#fff}
.band-rule{height:12px}
.band-rule::before{content:"";position:absolute;left:0;right:0;top:5px;height:1px;background:linear-gradient(90deg,rgba(255,255,255,.7),transparent)}
.band-rule::after{content:"";position:absolute;left:3px;top:1px;width:10px;height:10px;transform:rotate(45deg);background:linear-gradient(#9fc7e0,#6b8fb0)}
.news-item{top:1077px;width:175px;display:flex;gap:8px}
.date{width:31px;flex:none;text-align:center;font-weight:700}
.date .day{background:var(--blue);color:#fff;font-size:12px;height:17px;line-height:17px}
.date .mon{background:#fff;color:#333;font-size:8px;height:16px;line-height:16px}
.news-item h3{font-size:8.5px;font-weight:700;color:#fff}
.news-item p{font-size:8px;line-height:11px;color:#fff;margin-top:2px}
.band-split{left:469px;top:1032px;width:1px;height:92px;background:rgba(255,255,255,.4)}
.signup{left:485px;top:1076px;font-size:8px;font-weight:700;color:#fff}
.email{left:485px;top:1095px;width:134px;height:14px;background:#fff;font-size:7.5px;font-style:italic;color:#666;padding:3px 4px}
.submit{left:619px;top:1095px;width:43px;height:14px;background:var(--blue);color:#fff;font-size:7.5px;font-weight:700;text-align:center;line-height:14px}

/* footer */
.site-footer{left:0;top:1142px;width:743px;height:58px;background:var(--footer);color:#fff}
.footer-links{position:absolute;left:82px;top:15px;font-size:8px;font-weight:500}
.copyright{position:absolute;left:82px;top:36px;font-size:8px}
.foot-head{position:absolute;top:15px;font-size:8px;font-weight:500}
.cards{position:absolute;left:354px;top:32px;display:flex;gap:5px}
.cards i{width:23px;height:14px;border-radius:2px;background:#e9e9e9}
.socials{position:absolute;left:513px;top:31px;display:flex;gap:4px}
.socials i{width:14px;height:14px;background:#f0f0f0;border-radius:2px}
.eco-mark{position:absolute;left:630px;top:14px;width:32px;height:32px;border-radius:50%;background:#6dbb45}
</style>
</head>
<body>

<header>
  <div class="abs top-line"></div>
  <div class="abs account-tab login">
    <svg width="7" height="8" viewBox="0 0 7 8"><rect x="0" y="3.5" width="7" height="4.5" fill="#fff"/><path d="M1.5 3.5V2.2a2 2 0 0 1 4 0v1.3" stroke="#fff" fill="none"/></svg>Login</div>
  <div class="abs account-tab register">
    <svg width="8" height="8" viewBox="0 0 8 8"><circle cx="5.5" cy="2.5" r="2" fill="#fff"/><path d="M4.5 3.5 0.5 7.5" stroke="#fff" stroke-width="1.5"/></svg>Register</div>
  <div class="abs brand">Copper<br>Lantern</div>
  <div class="abs phone">
    <svg width="12" height="12" viewBox="0 0 24 24"><path fill="#1a7fc8" d="M6.6 10.8a15.1 15.1 0 0 0 6.6 6.6l2.2-2.2a1 1 0 0 1 1-.24 11.4 11.4 0 0 0 3.6.57 1 1 0 0 1 1 1V20a1 1 0 0 1-1 1A17 17 0 0 1 3 4a1 1 0 0 1 1-1h3.5a1 1 0 0 1 1 1c0 1.25.2 2.45.57 3.57a1 1 0 0 1-.25 1z"/></svg>
    0147 555 0192</div>
  <nav class="abs main-nav">
    <a class="active" href="#" style="width:70px">HOME</a>
    <a href="#" style="width:83px">ABOUT US</a>
    <a href="#" style="width:102px">BLOGS/EVENTS</a>
    <a href="#" style="width:93px">PURCHASE</a>
    <a href="#" style="width:100px;border-right:0">CONTACT US</a>
  </nav>
</header>

<section class="abs hero">
  <div class="abs art-car" role="img" aria-label="Glossy black sports car"></div>
  <div class="abs art-bottles" role="img" aria-label="Two spray bottles of the cleaner"></div>
  <div class="abs art-truck" role="img" aria-label="Illustration of a green 1950s pickup truck towing a vintage camper"></div>
  <div class="abs art-photo" role="img" aria-label="Hand spraying the cleaner onto a white surface"></div>
  <a class="abs shop-btn">Shop Our Products</a>
  <div class="abs shop-diamond" role="img" aria-label="Spray bottle of the cleaner"></div>
</section>
<div class="abs caption-bar">
  <h2>Waterless All Purpose Cleaner &amp; Protectant</h2>
  <div class="slider-dots"><i></i><i class="on"></i><i></i><i></i></div>
</div>

<section class="abs categories">
  <div class="category" style="left:107px"><div class="diamond"></div><div class="photo" role="img" aria-label="Motorhome RV" style="background:linear-gradient(#8a6e52,#d9d2c4)"></div><span>RVs</span></div>
  <div class="category" style="left:252px"><div class="diamond"></div><div class="photo" role="img" aria-label="White speedboat" style="background:linear-gradient(#f4f4f4,#6f7a86)"></div><span>BOATS</span></div>
  <div class="category" style="left:386px"><div class="diamond"></div><div class="photo" role="img" aria-label="Silver compact SUV" style="background:linear-gradient(#dcdcdc,#8a8f95)"></div><span>CARS</span></div>
  <div class="category" style="left:523px"><div class="diamond"></div><div class="photo" role="img" aria-label="Black cruiser motorcycle" style="background:linear-gradient(#9a9a9a,#1f1f1f)"></div><span>MOTORCYCLES</span></div>
</section>

<section>
  <h2 class="abs section-title" style="top:563px">Welcome to <span class="b">Copper</span> <span class="g">Lantern</span></h2>
  <div class="abs divider" style="top:586px"></div>
  <p class="abs lead" style="top:605px">Lorem ipsum dolor sit amet, consectetuer adipisemy nibh euismod tincidunt utre magmi aliquam erat volutpat. Ut wisi enimad minim veniam quis nostrutation ullaeipit lobortisi nisl ut aliquip ex ea commodo consequis autem veli eum ido inhendrer vulate velitm eonsequatvel illum dolore eu feugiat nulla facilisis at vero eros et accusao</p>
</section>

<section class="abs video-section"></section>
<h2 class="abs section-title" style="top:672px">See Our <span class="b">Training</span> <span class="g">Video</span></h2>
<div class="abs divider" style="top:695px"></div>
<p class="abs lead" style="top:716px">Lorem ipsum dolor sit amet, consectetuer adipisemy nibh euismod tincidunt utre magmi aliquam erat volutpat.</p>
<div class="abs monitor"></div>
<div class="abs monitor-chin"></div>
<div class="abs monitor-stand"></div>
<div class="abs video-screen" role="img" aria-label="Training video still: hand spraying the cleaner on a white vehicle"></div>
<div class="abs play-btn"></div>
<svg class="abs" style="left:366px;top:845px" width="12" height="14" viewBox="0 0 12 14"><path d="M0 0 12 7 0 14z" fill="#111"/></svg>

<section class="abs news-band"></section>
<h2 class="abs band-title" style="left:81px;top:1031px">News &amp; Events</h2>
<svg class="abs" style="left:441px;top:1034px" width="15" height="10" viewBox="0 0 15 10"><path d="M5 1 1 5l4 4M10 1l4 4-4 4" stroke="#fff" stroke-width="1.5" fill="none"/></svg>
<div class="abs band-rule" style="left:81px;top:1052px;width:370px"></div>
<article class="abs news-item" style="left:81px">
  <div class="date"><div class="day">17</div><div class="mon">JAN</div></div>
  <div><h3>Lorem ipsum dolor sitak ametn</h3><p>Lorem ipsum dolor sitak amet, co adipiscing elit, euismod poor.</p></div>
</article>
<article class="abs news-item" style="left:283px">
  <div class="date"><div class="day">17</div><div class="mon">JAN</div></div>
  <div><h3>Lorem ipsum dolor sitak ametn</h3><p>Lorem ipsum dolor sitak amet, co adipiscing elit, euismod poor.</p></div>
</article>
<div class="abs band-split"></div>
<h2 class="abs band-title" style="left:484px;top:1031px">Newletter</h2>
<div class="abs band-rule" style="left:484px;top:1052px;width:180px"></div>
<p class="abs signup">Sign up for a Newsletter and get updated!</p>
<div class="abs email">Enter email address</div>
<div class="abs submit">SUBMIT</div>

<footer class="abs site-footer">
  <div class="footer-links">Home &nbsp;/&nbsp; About Us &nbsp;/&nbsp; Blogs/Events &nbsp;/&nbsp; Parchase &nbsp;/&nbsp; Contact Us</div>
  <div class="copyright">© 2015 &nbsp;Copper Lantern. All Rights Reserved &nbsp;/&nbsp; Privacy Policy</div>
  <div class="foot-head" style="left:354px">Payment Methods We Accept</div>
  <div class="cards"><i></i><i></i><i></i><i></i></div>
  <div class="foot-head" style="left:513px">Socialize with us</div>
  <div class="socials"><i></i><i></i><i></i><i></i></div>
  <div class="eco-mark"></div>
</footer>

</body>
</html>
```